依頼詳細
新聞折込用のB4チラシの作成をお願いいたします。

9月20日の敬老の日に向けて、使用予定です。
・50〜60代向け
・健康的なイメージ
・写真をいれてほしい
(セラピストの写真は提供いたします。受け手が若い女性なので、受け手の顔を隠す・施術写真とは別に50〜60代の方の写真を入れるなどご対応お願いします。)

裏面は既存のデザインを利用予定のため、表面の作成をお願いいたします。
裏面のデザインを添付しますのでご参考していただけると幸いです。
https://48.parcelbox.jp/0913-8a27c5d1e9b04f36a2e8d71c5f0b94ae

ウェブでの展開も検討しておりますので、aiデータでいただきたいです。
記載項目
①「肩のお疲れ」「足腰のお疲れ」などお疲れの部位に訴えかけるワード

②「50代以上の方 限定クーポン」
1)60分以上のコース1,000円引き
2)平日はさらにお得!60分以上のコース1,500円引き

③治療目的ではないため保険は適用されません。の記載

④9月以外での利用も検討しているため、「敬老の日」という文言は不要です。

NGワード
・肩こり
・腰痛
・むくみ
ユルカゼーションのため、具体的症状や治療を連想させる文言はいれないようお願いいたします。
サイズ
B4
ページ数
片面
希望イメージ
シンプル 複雑
単色 カラフル
暗い 明るい
日常 高級
遊び心 厳粛
未来的 伝統的
女性的 男性的
希望する色
ブランドカラーは緑ですが、こだわり過ぎず
納品ファイル
• イラストレーター形式 (.ai)
補足説明
■ 選んだ理由

こちらのターゲット設定に対して、イメージと近いものでした。
普段のブランドでは出さない雰囲気で、試してみたいと思いました。

■ 提案者全員のお礼・コメント

ご応募いただきありがとうございました。
活用させていただきます。

```html
<!DOCTYPE html>
<html lang="ja">
<head>
<meta charset="utf-8">
<title>肩・足・腰 お疲れではありませんか? 50代以上の方 限定クーポン</title>
<link rel="stylesheet" href="https://fonts.googleapis.com/css2?family=Zen+Maru+Gothic:wght@500;700;900&family=Noto+Sans+JP:wght@400;500;700&display=swap">
<style>
  :root{
    --bg-top:#f3f8e4;
    --bg-bottom:#dcedbf;
    --leaf:#b9d98d;
    --teal:#2f9a86;
    --teal-dark:#2b6b5c;
    --orange:#f08a1e;
    --orange-deep:#e36f0c;
    --orange-pale:#fde7c8;
    --brown:#7a5a3a;
    --ink:#4a3d33;
    --white:#ffffff;
  }
  *{margin:0;padding:0;box-sizing:border-box}
  html,body{width:846px;height:1200px;overflow:hidden}
  body{font-family:"Noto Sans JP",sans-serif;color:var(--ink);background:#fff}
  .flyer{position:relative;width:846px;height:1200px;overflow:hidden;
    background:linear-gradient(180deg,var(--bg-top) 0%,#eaf4d4 45%,var(--bg-bottom) 100%)}
  .leaf-deco{position:absolute;opacity:.55;background:var(--leaf)}
  .leaf-deco.left{left:-40px;top:80px;width:150px;height:520px;border-radius:0 60% 0 60%}
  .leaf-deco.right{right:-30px;top:20px;width:120px;height:260px;opacity:.4;border-radius:50% 0 50% 0}

  .parts{position:absolute;left:48px;top:22px;display:flex;gap:10px;z-index:3}
  .parts span{width:92px;height:92px;border-radius:50%;background:var(--teal);color:var(--white);
    font-family:"Zen Maru Gothic",sans-serif;font-weight:900;font-size:60px;line-height:92px;text-align:center}

  .headline{position:absolute;left:52px;top:146px;z-index:3;font-family:"Zen Maru Gothic",sans-serif;
    font-weight:900;font-size:76px;line-height:1.18;color:var(--teal-dark);white-space:nowrap;
    text-shadow:0 0 6px rgba(255,255,255,.9),0 0 2px #fff}

  .photo{position:absolute}
  .photo.senior-woman{right:0;top:96px;width:300px;height:330px;
    background:linear-gradient(160deg,#e9e3d6,#c9b49a 60%,#8f7a68)}
  .photo.senior-man{left:168px;top:368px;width:256px;height:212px;border-radius:8px;
    background:linear-gradient(160deg,#efefe9,#cfc9bf 55%,#9a948b)}
  .photo.therapist{right:0;top:592px;width:424px;height:550px;
    background:linear-gradient(170deg,#e8efe0,#b9a78f 55%,#6b5a48)}

  .intro{position:absolute;left:440px;top:346px;width:400px;height:232px;border-radius:50%;
    background:rgba(255,255,255,.88);padding:30px 40px 0;z-index:2}
  .brand{display:flex;align-items:center;gap:10px;margin-left:28px}
  .brand i{width:14px;height:14px;border-radius:50%;background:var(--teal)}
  .brand b{font-family:"Zen Maru Gothic",sans-serif;font-weight:700;font-size:34px;color:var(--teal-dark);letter-spacing:3px}
  .intro p{margin-top:12px;font-size:13.5px;line-height:1.75;color:var(--ink);text-align:center}

  .coupon{position:absolute;left:56px;top:524px;width:424px;z-index:2}
  .coupon-head{background:var(--orange);color:var(--white);text-align:center;padding:14px 0 18px;
    font-family:"Zen Maru Gothic",sans-serif;font-weight:700;border-radius:8px 8px 0 0;position:relative}
  .coupon-head small{display:block;font-size:26px}
  .coupon-head strong{display:block;font-size:48px;font-weight:900;line-height:1.1}
  .coupon-head::after{content:"";position:absolute;left:50%;bottom:-18px;margin-left:-20px;
    border:20px solid transparent;border-top-color:var(--orange);border-bottom:0}
  .coupon-body{background:var(--orange-pale);padding:34px 24px 20px;border-radius:0 0 8px 8px}
  .ticket{background:var(--white);border:3px solid var(--orange);border-radius:8px;margin-bottom:22px;text-align:center;padding-bottom:12px}
  .ticket h3{background:var(--orange);color:var(--white);font-family:"Zen Maru Gothic",sans-serif;font-size:28px;font-weight:700;padding:4px 0}
  .ticket .course{font-size:26px;font-weight:500;margin-top:8px}
  .ticket .off{font-family:"Zen Maru Gothic",sans-serif;font-weight:900;color:var(--orange-deep);font-size:62px;line-height:1.1}
  .ticket .off em{font-style:normal;font-size:40px}
  .note{font-size:12px;color:var(--ink)}

  .badge{position:absolute;left:432px;top:846px;width:104px;height:104px;border-radius:50%;
    background:var(--orange-deep);border:3px solid var(--white);color:var(--white);
    font-family:"Zen Maru Gothic",sans-serif;font-weight:900;font-size:20px;line-height:1.25;
    display:flex;align-items:center;justify-content:center;text-align:center;z-index:4}

  .footer-bar{position:absolute;left:0;bottom:0;width:846px;height:58px;background:var(--brown);
    color:var(--white);display:flex;align-items:center;justify-content:flex-end;padding-right:30px;gap:8px;font-size:18px;font-weight:500;z-index:3}
</style>
</head>
<body>
<main class="flyer">
  <div class="leaf-deco left" role="img" aria-label="淡い緑の葉の装飾"></div>
  <div class="leaf-deco right" role="img" aria-label="淡い緑の葉と小鳥の装飾"></div>

  <div class="photo senior-woman" role="img" aria-label="腰に手を当てる50代女性の写真"></div>
  <div class="photo senior-man" role="img" aria-label="肩に手を当てる50代男性の写真"></div>
  <div class="photo therapist" role="img" aria-label="セラピストが施術する様子の写真(受け手の顔は映らない)"></div>

  <div class="parts"><span>肩</span><span>足</span><span>腰</span></div>
  <h1 class="headline">お疲れでは<br>ありませんか?</h1>

  <section class="intro">
    <div class="brand"><i></i><b>Yuruka</b></div>
    <p>注目したのは筋肉と体のめぐり。<br>筋肉に負担をかけず、体の質そのものを整える<br>ユルカ独自のボディケアとストレッチで<br>疲れをためない健康な毎日をサポートします。</p>
  </section>

  <section class="coupon">
    <div class="coupon-head"><small>50代以上の方</small><strong>限定クーポン</strong></div>
    <div class="coupon-body">
      <div class="ticket">
        <h3>クーポン1</h3>
        <p class="course">60分以上のコース</p>
        <p class="off">1,000<em>円引き</em></p>
      </div>
      <div class="ticket">
        <h3>クーポン2</h3>
        <p class="course">60分以上のコース</p>
        <p class="off">1,500<em>円引き</em></p>
      </div>
      <p class="note">※治療目的ではないため保険は適用されません。</p>
    </div>
  </section>

  <div class="badge">平日は<br>さらに<br>お得!</div>

  <footer class="footer-bar">裏面もご覧ください
    <svg width="18" height="18" viewBox="0 0 18 18"><circle cx="9" cy="9" r="9" fill="#fff"/><path d="M7 5l5 4-5 4z" fill="#7a5a3a"/></svg>
  </footer>
</main>
</body>
</html>
```